Pastry Trade Institute Website Homepage Revision

I need the "homepage" to the new Northfield Pastry Trade Institute to reworked. The current homepage is dull. It needs the attention of a professional graphic artist so it delivers a professionally finished feel and look. I have included the current URL for your viewing (builds.vorlimo.com/bridal-torte/cms/ ) to see where we are in the development phase. The elements on the homepage are all necessary and the colors are correct. I have also included the original Word document for the page (you can extract the RGB values and images from the doc). To be clear, I am not looking to recreate all the web pages, just the homepage. It needs to be responsive and stretched.

Target Market(s)

All bakers who sell wedding cakes in the United States

Number of Pages Required

1 page

Font styles to use
Other font styles liked:
• see the Word Document

Requirements
Must have
• It must have the elements already in the original mock up. That includes the colors and fonts.

```html
<!DOCTYPE html>
<html lang="en">
<head>
<meta charset="utf-8">
<title>Northfield Pastry Trade Institute</title>
<link href="https://fonts.googleapis.com/css2?family=Open+Sans:wght@400;600;700&family=Raleway:wght@500;700;800&display=swap" rel="stylesheet">
<style>
:root{
  --rose:#c8576a;
  --rose-dark:#a9404f;
  --rose-pale:#f6e4e7;
  --ink:#4a4a4a;
  --muted:#8a8a8a;
  --line:#dddddd;
  --panel:#eeeae3;
  --form:#e9e9e9;
  --btn:#6f6f6f;
  --footer:#262626;
  --footer-text:#9a9a9a;
  --white:#ffffff;
}
*{box-sizing:border-box;margin:0;padding:0}
html,body{width:1200px;height:2856px;overflow:hidden;background:var(--white)}
body{font-family:"Open Sans",Arial,sans-serif;color:var(--ink);font-size:13px;line-height:1.5;position:relative}
.side-flora{position:absolute;width:170px;height:420px;border-radius:50%;background:radial-gradient(circle,#f3d3d9 0%,#fbeef0 55%,rgba(255,255,255,0) 75%);opacity:.8}
.side-flora.left-a{left:-60px;top:900px}
.side-flora.right-a{right:-60px;top:820px}
.side-flora.left-b{left:-70px;top:1480px}
.side-flora.right-b{right:-60px;top:1380px}

/* header */
.site-header{height:112px;position:relative;border-bottom:1px solid var(--line)}
.brand{position:absolute;left:200px;top:22px;display:flex;align-items:center;gap:10px}
.brand-dot{width:34px;height:34px;border-radius:50%;background:var(--rose)}
.brand-name{font-family:"Raleway",sans-serif;font-weight:700;color:var(--rose);font-size:15px;line-height:1.2;width:150px}
.cta-top{position:absolute;right:200px;top:26px;background:var(--rose);color:var(--white);font-family:"Raleway",sans-serif;font-weight:700;font-size:11px;letter-spacing:1px;padding:8px 18px;border-radius:3px}
.main-nav{position:absolute;right:200px;top:76px;display:flex;gap:26px;font-family:"Raleway",sans-serif;font-weight:700;font-size:9.5px;letter-spacing:.6px;color:var(--rose);white-space:nowrap}

/* hero */
.hero{height:608px;background:radial-gradient(ellipse at 50% 55%,#f1e6ea 0%,#b9768f 18%,#6a2447 45%,#2f0f26 80%);}

/* media strip */
.media-strip{height:90px;display:flex;justify-content:center;align-items:center;gap:58px;border-bottom:1px solid var(--line)}
.media-badge{width:70px;height:34px;background:#cfcfcf;border-radius:3px}

/* video + form */
.intro{height:360px;position:relative}
.video{position:absolute;left:248px;top:42px;width:552px;height:274px;background:linear-gradient(135deg,#3a2a30,#6b4a55 50%,#2a1e22);}
.video-play{position:absolute;left:246px;top:96px}
.video-bar{position:absolute;left:0;right:0;bottom:0;height:30px;background:rgba(0,0,0,.75);display:flex;align-items:center;padding:0 12px;gap:12px}
.video-track{flex:1;height:4px;background:#555;border-radius:2px;position:relative}
.video-track::before{content:"";position:absolute;left:0;top:0;width:30%;height:4px;background:var(--rose);border-radius:2px}
.optin{position:absolute;left:820px;top:42px;width:180px;background:var(--form);padding:18px 14px;text-align:center}
.optin h3{font-family:"Raleway",sans-serif;font-weight:500;font-size:13px;color:var(--ink);line-height:1.35;margin-bottom:12px}
.field{height:24px;background:var(--white);border:1px solid var(--line);font-size:10px;color:#aaa;text-align:left;padding:4px 8px;margin-bottom:7px}
.btn-rose{display:inline-block;background:var(--rose);color:var(--white);font-size:10px;font-weight:600;padding:5px 18px;border-radius:3px;margin-top:4px}

/* headings */
.section-title{text-align:center;font-family:"Raleway",sans-serif;font-weight:800;font-size:23px;line-height:1.2;color:var(--rose);letter-spacing:.5px}
.section-sub{text-align:center;font-size:10.5px;color:var(--muted);margin-top:6px}

/* marketing */
.marketing{height:260px;padding-top:34px;border-top:1px solid var(--line)}
.choice-row{display:flex;justify-content:center;gap:20px;margin-top:22px}
.choice{width:180px;height:142px;background:var(--panel);text-align:center;padding:22px 14px}
.choice h4{font-family:"Raleway",sans-serif;font-weight:700;font-size:12px;color:var(--ink);line-height:1.35;height:52px}
.btn-grey{display:inline-block;background:var(--btn);color:var(--white);font-size:10px;font-weight:600;padding:5px 18px;border-radius:12px;line-height:1.4}

/* sales */
.sales{height:420px;padding-top:30px}
.card-row{display:flex;justify-content:center;gap:20px;margin-top:18px}
.card{width:226px;height:272px;border:5px solid var(--rose);text-align:center;background:var(--white);display:flex;flex-direction:column;align-items:center}
.card-photo{height:140px;width:100%}
.card p{font-size:10px;color:var(--ink);padding:10px 14px 6px;line-height:1.45;height:74px}
.card .btn-grey{margin-top:6px}
.card-photo.one{background:linear-gradient(160deg,#d8d3cf,#7a3238 60%,#2b2226)}
.card-photo.two{background:linear-gradient(160deg,#e8e1dc,#8f7462 55%,#3c2e29)}
.card-photo.three{background:linear-gradient(160deg,#f3eee9,#c9b79e 55%,#6f6156)}

/* band */
.band{height:420px;background:var(--rose);position:relative;color:var(--white)}
.band-photo{position:absolute;left:248px;top:140px;width:232px;height:200px;background:linear-gradient(160deg,#f1ece6,#d9b8a4 50%,#5a6c86);border:4px solid var(--white)}
.band-copy{position:absolute;left:540px;top:70px;width:420px}
.band-copy h2{font-family:"Raleway",sans-serif;font-weight:800;font-size:16px;line-height:1.4;margin-bottom:18px}
.band-copy p{font-size:11px;line-height:1.6;margin-bottom:14px;color:#fbe9ec}

/* newsletter */
.newsletter{height:300px;position:relative}
.newsletter-copy{position:absolute;left:240px;top:60px;width:520px;font-size:12.5px;line-height:1.6}
.newsletter-copy p{margin-bottom:18px}
.newsletter-copy strong{color:var(--rose)}
.signup{position:absolute;left:820px;top:52px;width:180px;background:var(--form);padding:16px 14px;text-align:center}
.signup small{display:block;font-size:8px;color:var(--muted);margin-top:8px;line-height:1.4}

/* footer */
.site-footer{height:286px;background:var(--footer);position:relative;color:var(--footer-text)}
.footer-cols{position:absolute;left:240px;right:200px;top:36px;display:flex;justify-content:space-between}
.footer-col h5{font-family:"Raleway",sans-serif;font-weight:700;font-size:11px;color:var(--rose);margin-bottom:10px}
.footer-col li{list-style:none;font-size:9.5px;line-height:1.75}
.copyright{position:absolute;left:0;right:0;bottom:26px;text-align:center;font-size:9px;color:#777}
</style>
</head>
<body>
<div class="side-flora left-a" role="img" aria-label="Pale rose flowers"></div>
<div class="side-flora right-a" role="img" aria-label="Pale rose flowers"></div>
<div class="side-flora left-b" role="img" aria-label="Pale rose flowers"></div>
<div class="side-flora right-b" role="img" aria-label="Pale rose flowers"></div>

<header class="site-header">
  <div class="brand"><span class="brand-dot"></span><span class="brand-name">Northfield Pastry Trade Institute</span></div>
  <div class="cta-top">GET STARTED NOW</div>
  <nav class="main-nav">
    <span>HOME</span><span>GET STARTED</span><span>MARKETING SOLUTIONS</span><span>SALES SOLUTIONS</span><span>ABOUT US</span><span>CONTACT</span><span>ORDER PRODUCTS</span><span>BLOG</span>
  </nav>
</header>

<section class="hero" role="img" aria-label="Tiered white wedding cake with pink flowers on a candlelit table with champagne"></section>

<section class="media-strip" aria-label="As featured in">
  <span class="media-badge"></span><span class="media-badge"></span><span class="media-badge"></span><span class="media-badge"></span><span class="media-badge"></span><span class="media-badge"></span><span class="media-badge"></span>
</section>

<section class="intro">
  <div class="video" role="img" aria-label="Introductory video still with title overlay">
    <svg class="video-play" width="60" height="60" viewBox="0 0 60 60"><circle cx="30" cy="30" r="27" fill="none" stroke="#fff" stroke-width="3"/><path d="M24 18 L42 30 L24 42 Z" fill="#fff"/></svg>
    <div class="video-bar">
      <svg width="12" height="12" viewBox="0 0 12 12"><path d="M2 1 L11 6 L2 11 Z" fill="#fff"/></svg>
      <div class="video-track"></div>
      <svg width="14" height="12" viewBox="0 0 14 12"><path d="M1 4 H4 L8 1 V11 L4 8 H1 Z" fill="#fff"/></svg>
    </div>
  </div>
  <form class="optin">
    <h3>Have a New Discovery That Sells More Wedding Cakes and at Higher Prices!</h3>
    <div class="field">Your Name</div>
    <div class="field">Your Email</div>
    <div class="field">Your Phone</div>
    <span class="btn-rose">Watch Now</span>
  </form>
</section>

<section class="marketing">
  <h2 class="section-title">MARKETING SOLUTIONS</h2>
  <p class="section-sub">Our research-based marketing tools help you attract more brides and grow your wedding cake business.</p>
  <div class="choice-row">
    <div class="choice"><h4>I'm New to Selling Wedding Cakes...</h4><span class="btn-grey">Click Here</span></div>
    <div class="choice"><h4>I Want to Maintain My Wedding Sales...</h4><span class="btn-grey">Click Here</span></div>
    <div class="choice"><h4>I'm Eager to Boost My Sales and Profits...</h4><span class="btn-grey">Click Here</span></div>
    <div class="choice"><h4>I'm Ready to Dominate My Market Area...</h4><span class="btn-grey">Click Here</span></div>
  </div>
</section>

<section class="sales">
  <h2 class="section-title">SALES SOLUTIONS</h2>
  <p class="section-sub">Learn proven sales scripts and consultation methods that turn tastings into signed orders.</p>
  <div class="card-row">
    <div class="card"><div class="card-photo one" role="img" aria-label="Bakery team in white uniforms"></div><p>Discover the Bridal Consult Scripts that turn first meetings into booked wedding cake orders every week.</p><span class="btn-grey">Learn More</span></div>
    <div class="card"><div class="card-photo two" role="img" aria-label="Couple meeting a cake designer"></div><p>See how top bakers present pricing with confidence and close more high value weddings.</p><span class="btn-grey">Learn More</span></div>
    <div class="card"><div class="card-photo three" role="img" aria-label="Bride considering options"></div><p>Understand what brides truly want and use simple steps to become their first choice.</p><span class="btn-grey">Learn More</span></div>
  </div>
</section>

<section class="band">
  <div class="band-photo" role="img" aria-label="Portrait of the institute founder"></div>
  <div class="band-copy">
    <h2>Use Cutting-edge Methods Proven to Generate MORE Leads, Convince MORE Brides to Choose You, Get HIGHER Prices and DOMINATE Your Competition.</h2>
    <p>Our breakthrough marketing and sales methods are possible due to the many years of research conducted with over one thousand brides across the country, revealing how they decide and which bakers they trust.</p>
    <p>From the findings, we have developed new and revolutionary marketing strategies, sales tools, and a complete consultation system. Now you can use the same proven steps to win the brides that matter most to your bakery.</p>
  </div>
</section>

<section class="newsletter">
  <div class="newsletter-copy">
    <p>Enter Your Name and Email Address Below. Each month you'll receive our "Advanced Wedding Cake Marketing Advisory." It's normally available for a $397 subscription fee. You'll receive the first year... absolutely FREE.</p>
    <p>Join our <strong>"Insider Advisory"</strong> for FREE! You'll receive the latest research secrets while learning how to use psychology for getting a decisive advantage to market and sell your wedding cakes.</p>
  </div>
  <form class="signup">
    <div class="field">Your Name</div>
    <div class="field">Your Email</div>
    <span class="btn-rose">Sign Me Up</span>
    <small>We respect your privacy and will never share your email address with anyone.</small>
  </form>
</section>

<footer class="site-footer">
  <div class="footer-cols">
    <div class="footer-col"><h5>Marketing Solutions</h5><ul><li>Creating the Perfect Cake Brand</li><li>Advanced Marketing Videos</li><li>Wedding Show Planning</li><li>Bridal Lead Generation</li><li>Website Review Service</li><li>Social Media Guidance</li><li>Referral Partner Program</li></ul></div>
    <div class="footer-col"><h5>Sales Solutions</h5><ul><li>Bridal Consult Scripts</li><li>Tasting Presentation Kit</li><li>Pricing With Confidence</li><li>Follow Up Templates</li><li>Closing Techniques</li></ul></div>
    <div class="footer-col"><h5>About Us</h5><ul><li>Our Research</li><li>Our Team</li><li>Testimonials</li><li>Speaking</li></ul></div>
    <div class="footer-col"><h5>Contact With Us</h5><ul><li>Contact Form</li><li>Support</li></ul></div>
    <div class="footer-col"><h5>Recent Blog Posts</h5><ul><li>Five Tasting Mistakes</li><li>Pricing Tiers That Sell</li></ul></div>
  </div>
  <p class="copyright">© Northfield Pastry Trade Institute. All rights reserved. Privacy Policy | Terms of Use</p>
</footer>
</body>
</html>
```